Verostel business card

Business card for sustainable investment company called "Verostel". Verostel is an exchange platform selling carbon credits between buyers and sellers. Carbon Credits are an environmental commodity for reducing global carbon emissions.

the card should obviously have our logo and the theme should be sustainability/environment mixed with a trading platform.

Contact Information for Business Card

Logo, Name, Title, Phone, Email

Colors
0054AA
0677BA
7BADD7
CADEEF
E8F1F8
0094D4
00A9DD
6FCCEA
C7EBF8
E9F6FB
00AB8E
00BBA5
67D7C9
C6EFE9
E9F9F6
59FF00
82FF00
B8FF75
E3FFCB
F4FFEA

```html
<!DOCTYPE html>
<html lang="en">
<head>
<meta charset="utf-8">
<title>Verostel business card</title>
<link rel="stylesheet" href="https://fonts.googleapis.com/css2?family=Montserrat:wght@500;700;800&family=Lato:wght@400;700&display=swap">
<style>
  :root {
    --stage: #e6e9ee;
    --card-navy: #142a52;
    --accent-cyan: #4cc6e3;
    --accent-blue: #3a8fd6;
    --divider: #45bcdc;
    --text-white: #ffffff;
    --text-soft: #dfe8f3;
  }
  * { margin: 0; padding: 0; box-sizing: border-box; }
  html, body {
    width: 1200px; height: 856px; overflow: hidden;
    background: var(--stage);
  }
  .stage {
    position: relative; width: 1200px; height: 856px;
    display: flex; flex-direction: column; align-items: center; justify-content: center; gap: 28px;
  }
  .card {
    position: relative; width: 700px; height: 400px;
    background: var(--card-navy);
    color: var(--text-white);
    box-shadow: 0 6px 18px rgba(20, 42, 82, 0.18);
  }
  /* brand lockup */
  .brand { display: flex; flex-direction: column; align-items: flex-start; }
  .brand-square {
    display: block; width: 40px; height: 40px;
    background: linear-gradient(135deg, var(--accent-cyan), var(--accent-blue));
    margin-bottom: 14px;
  }
  .brand-name {
    font-family: "Montserrat", sans-serif; font-weight: 700;
    text-transform: uppercase; letter-spacing: 0.5px;
    color: var(--text-white); line-height: 1;
  }
  /* contact side */
  .card-contact .brand {
    position: absolute; left: 70px; top: 130px;
  }
  .card-contact .brand-name { font-size: 34px; }
  .divider {
    position: absolute; left: 345px; top: 75px;
    width: 2px; height: 250px; background: var(--divider);
  }
  .person {
    position: absolute; left: 385px; top: 100px;
  }
  .person-name {
    font-family: "Montserrat", sans-serif; font-weight: 800;
    font-size: 25px; color: var(--accent-cyan); text-transform: uppercase; line-height: 1.1;
  }
  .person-title {
    font-family: "Lato", sans-serif; font-size: 17px; color: var(--text-soft);
    margin-top: 4px;
  }
  .contact-list { list-style: none; margin-top: 22px; }
  .contact-item {
    display: flex; align-items: center; gap: 10px;
    font-family: "Lato", sans-serif; font-size: 17px; color: var(--text-soft);
    line-height: 1.55;
  }
  .contact-icon { width: 15px; height: 15px; flex: none; }
  /* logo side */
  .card-logo .brand {
    position: absolute; left: 50%; top: 50%; transform: translate(-50%, -50%);
    align-items: flex-start;
  }
  .card-logo .brand-square { width: 80px; height: 80px; margin-bottom: 26px; }
  .card-logo .brand-name { font-size: 62px; }
</style>
</head>
<body>
<main class="stage">
  <section class="card card-contact" aria-label="Business card front">
    <div class="brand">
      <span class="brand-square"></span>
      <span class="brand-name">Verostel</span>
    </div>
    <div class="divider"></div>
    <div class="person">
      <h1 class="person-name">Daniel Hart</h1>
      <p class="person-title">Managing Director</p>
      <ul class="contact-list">
        <li class="contact-item">
          <svg class="contact-icon" viewBox="0 0 16 16" aria-hidden="true"><path fill="#4cc6e3" d="M3.5 1.5l2.5 0 1 3.5-1.8 1.2a8 8 0 0 0 4.6 4.6L11 9l3.5 1v2.5c0 1-1 2-2 2A11 11 0 0 1 1.5 3.5c0-1 1-2 2-2z"/></svg>
          <span>987 654 321</span>
        </li>
        <li class="contact-item">
          <svg class="contact-icon" viewBox="0 0 16 16" aria-hidden="true"><rect x="1" y="3" width="14" height="10" rx="1.5" fill="#4cc6e3"/><path d="M1.5 4l6.5 5 6.5-5" fill="none" stroke="#142a52" stroke-width="1.4"/></svg>
          <span>info@verostel.com</span>
        </li>
        <li class="contact-item">
          <svg class="contact-icon" viewBox="0 0 16 16" aria-hidden="true"><circle cx="8" cy="8" r="6.8" fill="none" stroke="#4cc6e3" stroke-width="1.5"/><ellipse cx="8" cy="8" rx="3" ry="6.8" fill="none" stroke="#4cc6e3" stroke-width="1.2"/><path d="M1.2 8h13.6" stroke="#4cc6e3" stroke-width="1.2"/></svg>
          <span>www.verostel.com</span>
        </li>
      </ul>
    </div>
  </section>

  <section class="card card-logo" aria-label="Business card back">
    <div class="brand">
      <span class="brand-square"></span>
      <span class="brand-name">Verostel</span>
    </div>
  </section>
</main>
</body>
</html>
```